Sports Nutrition line needs new label look/feel

We need a new label design for "Telmo",our Sports Nutrition line of vitamins, nutraceuticals, protein powders, and performance endurance products. We would like to see two separate designs, one blue and one red, as these are the two colors we are torn between. The labels should have the look/feel of a sports or fitness label, bold coloring, lettering, and even some use of holographic foiling.
Brands we would be similar to those found on pulsevaultshop.com and stridecraftnow.com. Brands we like in particular are QRT and Velmot.

Target Market(s)

Fitness enthusiasts,athletes, health nuts..

Industry/Entity Type

Nutrition

Font styles to use
Sans Serif
Decorative
Script

Colors
ec1f27
0692cd
0355a3
3276b5
f04a50

Requirements
Must have
• -Fitness look/feel
• -bold colors (preferably red and blue)
• -use of icons (eye health, brain, health, etc.)
• -"Fit" in "TelMO" must stand out
• -use tagline "Building Healthy Bodies"
Nice to have
• -holographic foiling elements
• -try to incorporate a molecular element (like those shown in the example labels)
Should not have
• -Light, calming colors
• -difficult to read fonts

```html
<!DOCTYPE html>
<html lang="en">
<head>
<meta charset="utf-8">
<title>TelMO – Label</title>
<link rel="stylesheet" href="https://fonts.googleapis.com/css2?family=Montserrat:wght@400;500;600;800&display=swap">
<style>
  :root {
    --page-bg: #ffffff;
    --brand-blue: #0355a3;
    --brand-blue-deep: #0b4596;
    --brand-blue-light: #3276b5;
    --silver-light: #f4f5f7;
    --silver-mid: #d9dce1;
    --silver-dark: #a9adb4;
    --text-grey: #3a3d42;
    --white: #ffffff;
  }
  * { margin: 0; padding: 0; box-sizing: border-box; }
  html, body {
    width: 1200px; height: 960px; overflow: hidden;
    background: var(--page-bg);
    font-family: "Montserrat", sans-serif;
  }
  .canvas { position: relative; width: 1200px; height: 960px; }
  .label {
    position: absolute; left: 250px; top: 110px;
    width: 700px; height: 730px;
  }
  .label-shape { position: absolute; inset: 0; }
  .brand-name {
    position: absolute; left: 0; right: 0; top: 200px;
    text-align: center;
    font-weight: 600; font-size: 100px; letter-spacing: 2px;
    color: var(--white); line-height: 1;
  }
  .tagline {
    position: absolute; left: 0; right: 0; top: 400px;
    text-align: center;
    font-weight: 800; font-size: 38px; letter-spacing: 1px;
    color: var(--brand-blue);
  }
  .tagline-rule {
    position: absolute; left: 70px; right: 70px; top: 452px;
    height: 2px; background: linear-gradient(90deg, transparent, var(--silver-dark), transparent);
  }
  .subtitle {
    position: absolute; left: 0; right: 0; top: 462px;
    text-align: center;
    font-weight: 400; font-size: 27px;
    color: var(--text-grey);
  }
  .benefit-icons {
    position: absolute; left: 0; right: 0; top: 530px;
    display: flex; justify-content: center; gap: 22px;
  }
  .benefit-icon {
    width: 50px; height: 50px; border-radius: 50%;
    border: 2px solid var(--text-grey);
    display: flex; align-items: center; justify-content: center;
    background: var(--white);
  }
  .benefit-icon span {
    width: 28px; height: 28px; border-radius: 50%;
    background: radial-gradient(circle, var(--brand-blue-light), var(--brand-blue));
  }
  .supply-line {
    position: absolute; left: 0; right: 0; top: 612px;
    text-align: center;
    font-weight: 800; font-size: 19px;
    color: var(--brand-blue);
  }
</style>
</head>
<body>
<main class="canvas">
  <section class="label">
    <svg class="label-shape" width="700" height="730" viewBox="0 0 700 730">
      <defs>
        <clipPath id="label-outline">
          <path d="M0 0 H700 V650 Q350 760 0 650 Z"/>
        </clipPath>
        <linearGradient id="silver-fill" x1="0" y1="0" x2="1" y2="1">
          <stop offset="0" stop-color="#e3e5e9"/>
          <stop offset="0.45" stop-color="#f6f7f9"/>
          <stop offset="1" stop-color="#cfd2d7"/>
        </linearGradient>
        <linearGradient id="blue-fill" x1="0" y1="0" x2="1" y2="1">
          <stop offset="0" stop-color="#0b4596"/>
          <stop offset="0.5" stop-color="#1a5eb0"/>
          <stop offset="1" stop-color="#0355a3"/>
        </linearGradient>
        <linearGradient id="rim" x1="0" y1="0" x2="1" y2="0">
          <stop offset="0" stop-color="#9aa0a8"/>
          <stop offset="0.5" stop-color="#ffffff"/>
          <stop offset="1" stop-color="#9aa0a8"/>
        </linearGradient>
      </defs>
      <g clip-path="url(#label-outline)">
        <rect width="700" height="730" fill="url(#silver-fill)"/>
        <path class="top-band" d="M0 0 H700 V370 Q350 250 0 370 Z" fill="url(#blue-fill)"/>
        <path d="M0 370 Q350 250 700 370" fill="none" stroke="url(#rim)" stroke-width="6"/>
        <path class="bottom-swoosh-left" d="M0 520 Q90 660 330 700 L0 730 Z" fill="#0355a3"/>
        <path d="M0 565 Q120 680 330 700 L0 730 Z" fill="#0b4596"/>
        <path class="bottom-swoosh-right" d="M700 520 Q610 660 370 700 L700 730 Z" fill="#0355a3"/>
        <path d="M700 565 Q580 680 370 700 L700 730 Z" fill="#0b4596"/>
        <path d="M0 650 Q350 760 700 650" fill="none" stroke="url(#rim)" stroke-width="10"/>
      </g>
      <path d="M0 0 H700 V650 Q350 760 0 650 Z" fill="none" stroke="url(#rim)" stroke-width="6"/>
    </svg>

    <h1 class="brand-name">TelMO</h1>
    <p class="tagline">BUILDING HEALTHY BODIES</p>
    <div class="tagline-rule"></div>
    <p class="subtitle">Antioxidant Formula to Boost Immunity</p>
    <div class="benefit-icons">
      <div class="benefit-icon"><span role="img" aria-label="Joint health icon"></span></div>
      <div class="benefit-icon"><span role="img" aria-label="Brain health icon"></span></div>
      <div class="benefit-icon"><span role="img" aria-label="Hair health icon"></span></div>
      <div class="benefit-icon"><span role="img" aria-label="Eye health icon"></span></div>
      <div class="benefit-icon"><span role="img" aria-label="Digestive health icon"></span></div>
    </div>
    <p class="supply-line">90 Day Supply Dietary Supplement</p>
  </section>
</main>
</body>
</html>
```